Commercial Auto Insurance Application and Commercial Property Insurance Application

Hi I need a fillable application for my business to send to potential clients for Commercial Auto Insurance and Commercial Property Insurance. I have attached an example application I currently use for another line of insurance.
Commercial Auto Insurance Application
On the first page I would need the following:
- Business Name: (fill in area for text)
- Effective Date: (fill in area for text)
- How do you structure your business? (Check box for “Sole Proprietor”, “Partnership”, “Corporation”, “LLC”)
- Contact Name: (fill in area for text) / Phone Number: (fill in area for text) / Contact Email (fill in area for text)
- Mailing address: (fill in area for text)
- Garaging location: (fill in area for text)
- Owner Name: (fill in area for text)
- Description of Operations: (fill in area for text)
- How long has the operation been in business? (fill in area for text)
- How many years of experience does your management have in the truck/transportation industry? (fill in area for text)
Coverages
Liability Combined Single Limit: ($1,000,000 (checkbox) / $500,000 (checkbox / $300,000 (checkbox) / Other: (fill in area for text)
Uninsured Motorist CSL: (fill in area for text) (checkbox for “Rejected”)
Medical Payments: (fill in area for text)
Physical Damage: (fill in area for text) (checkbox for Rejected)
Liability Deducible: ($500 checkbox, $1,000 checkbox, $2,500 checkbox, $5,000 checkbox)
Physical Damage Deductible: ($500 checkbox, $1,000 checkbox, $2,500 checkbox, $5,000 checkbox)
Driving radius: (fill in area for text)
How many years have you had your own continuous commercial auto insurance coverage for the current business name? (fill in area for text)
Do any of your vehicles travel across state lines? Yes (checkbox)/ No (checkbox)
If yes, please list all states in which vehicles operate: (fill in area for text)
What is the maximum radius traveled for your customer's business?
0-25 miles (checkbox)
26-50 miles (checkbox)
51-75 miles (checkbox)
76-100 miles (checkbox)
101-150 miles (checkbox)
151-200 miles (checkbox)
201-300 miles (checkbox)
300+ miles (checkbox)
Would you like physical damage coverage for this vehicle? (should be for each vehicle listed)
On the 2nd page of the application I would need the following:
I would need to have it where people can fill in the vehicle information such as VIN:, Year:, Make:, Model:, Type of Vehicle:, Trailers:, Value:
I would also need to have it where people can fill in the drivers with their driver info including Name:, DOB:, DL #:, DL State:, Class of License:, Married: Yes/No, Number of years driving similar vehicle:
Please make it where you can fill in 20 vehicle's information and 20 driver's info.
For the 2nd Application I would need one for Property Insurance
On the Commercial Property Application I would need the following:
- Building Address: (fill in area for text)
- Building Description: (fill in area for text)
- Building Amount: $(fill in area for text)
- Business Personal Property Amount: $ (fill in area for text) (checkbox for Not Needed)
- Building Sq Ft: (fill in area for text)
- Total Area Sq Ft: (fill in area for text)
- Building Construction Type: Wood Frame (checkbox), Steel (checkbox), Fire Resistive (checkbox), Non-Combustible (checkbox), Other (fill in area for text)
- # of stories: (fill in area for text)
- Year Built: (fill in area for text)
- Wiring improvement year: (fill in area for text)
- Roofing improvement year: (fill in area for text)
- Plumbing improvement year: (fill in area for text)
- Heating improvement year: (fill in area for text)
- What is to the right of the building and distance: (fill in area for text)
- What is to the left of the building and distance: (fill in area for text)
- What is in front of the building and distance: (fill in area for text)
- What is behind the building and distance: (fill in area for text)
- Burglar alarm installation and serviced by: (fill in area for text) None (checkbox)
- Does the premises have fire protection? Sprinkler system (checkbox), Fire detection (checkbox), Other: (fill in area for text) None (checkbox)

```html
<!DOCTYPE html>
<html lang="en">
<head>
<meta charset="utf-8">
<title>Commercial Auto Insurance Application</title>
<link rel="stylesheet" href="https://fonts.googleapis.com/css2?family=Arimo:wght@400;700&family=Montserrat:wght@800;900&display=swap">
<style>
  :root {
    --backdrop: #e9e9e9;
    --paper: #ffffff;
    --accent: #f15a29;
    --field: #f4f3e5;
    --ink: #111111;
    --rule: #222222;
  }
  * { margin: 0; padding: 0; box-sizing: border-box; }
  html, body { width: 1199px; height: 1200px; overflow: hidden; }
  body { background: var(--backdrop); font-family: "Arimo", Arial, sans-serif; color: var(--ink); }
  .application {
    position: absolute; left: 137px; top: 0; width: 925px; height: 1200px;
    background: var(--paper);
  }
  .title-band {
    position: absolute; left: 0; top: 0; width: 100%; height: 70px;
    background: var(--accent); color: #fff;
    font-family: "Montserrat", Arial, sans-serif; font-weight: 800;
    font-size: 29px; letter-spacing: 0.3px;
    display: flex; align-items: center; justify-content: center;
  }
  .form-frame {
    position: absolute; left: 14px; top: 70px; width: 897px; height: 1116px;
    border: 2px solid var(--rule); border-top: none;
  }
  .label { position: absolute; font-size: 15px; line-height: 20px; white-space: nowrap; transform: translateY(-10px); }
  .field { position: absolute; height: 20px; background: var(--field); transform: translateY(-10px); }
  .field.tall { transform: none; }
  .check { position: absolute; width: 19px; height: 19px; background: var(--field); transform: translateY(-10px); }
  .section-title {
    position: absolute; right: 28px; top: 512px;
    font-family: "Montserrat", Arial, sans-serif; font-weight: 900; font-size: 30px; letter-spacing: 0.5px;
  }
</style>
</head>
<body>
<main class="application">
  <header class="title-band">COMMERCIAL AUTO INSURANCE APPLICATION</header>
  <div class="form-frame"></div>

  <span class="label" style="left:42px;top:96px">Business Name:</span>
  <span class="field" style="left:159px;top:96px;width:466px"></span>
  <span class="label" style="left:640px;top:96px">Effective Date:</span>
  <span class="field" style="left:787px;top:96px;width:109px"></span>

  <span class="label" style="left:42px;top:131px">How do you structure your business?</span>
  <span class="label" style="left:42px;top:166px">Sole Proprietor</span>
  <span class="check" style="left:149px;top:166px"></span>
  <span class="label" style="left:205px;top:166px">Partnership</span>
  <span class="check" style="left:296px;top:166px"></span>
  <span class="label" style="left:367px;top:166px">Corporation</span>
  <span class="check" style="left:459px;top:166px"></span>
  <span class="label" style="left:530px;top:166px">LLC</span>
  <span class="check" style="left:575px;top:166px"></span>

  <span class="label" style="left:42px;top:201px">Contact Name:</span>
  <span class="field" style="left:149px;top:201px;width:156px"></span>
  <span class="label" style="left:312px;top:201px">Phone Number:</span>
  <span class="field" style="left:427px;top:201px;width:149px"></span>
  <span class="label" style="left:584px;top:201px">Contact Email:</span>
  <span class="field" style="left:688px;top:201px;width:208px"></span>

  <span class="label" style="left:42px;top:236px">Mailing address:</span>
  <span class="field" style="left:159px;top:236px;width:737px"></span>
  <span class="label" style="left:42px;top:271px">Garaging location:</span>
  <span class="field" style="left:172px;top:271px;width:724px"></span>
  <span class="label" style="left:42px;top:306px">Owner Name:</span>
  <span class="field" style="left:141px;top:306px;width:755px"></span>

  <span class="label" style="left:42px;top:341px">Description of Operations:</span>
  <span class="field tall" style="left:42px;top:357px;width:854px;height:38px"></span>
  <span class="label" style="left:42px;top:410px">How long has the operation been in business?</span>
  <span class="field tall" style="left:42px;top:424px;width:854px;height:38px"></span>
  <span class="label" style="left:42px;top:480px">How many years of experience does your management have in the truck/transportation industry?</span>
  <span class="field" style="left:696px;top:480px;width:200px"></span>

  <h2 class="section-title">COVERAGES</h2>
  <span class="label" style="left:42px;top:544px">Liability Combined Single Limit:</span>
  <span class="label" style="left:42px;top:579px">$1,000,000</span>
  <span class="check" style="left:130px;top:579px"></span>
  <span class="label" style="left:205px;top:579px">$500,000</span>
  <span class="check" style="left:272px;top:579px"></span>
  <span class="label" style="left:367px;top:579px">$300,000</span>
  <span class="check" style="left:442px;top:579px"></span>
  <span class="label" style="left:530px;top:579px">Other:</span>
  <span class="field" style="left:582px;top:579px;width:314px"></span>

  <span class="label" style="left:42px;top:614px">Uninsured Motorist CSL:</span>
  <span class="field" style="left:218px;top:614px;width:351px"></span>
  <span class="label" style="left:584px;top:614px">Rejected</span>
  <span class="label" style="left:42px;top:649px">Medical Payments:</span>
  <span class="field" style="left:218px;top:649px;width:351px"></span>
  <span class="label" style="left:42px;top:684px">Physical Damage:</span>
  <span class="field" style="left:218px;top:684px;width:351px"></span>
  <span class="label" style="left:584px;top:684px">Rejected</span>
  <span class="check" style="left:656px;top:684px"></span>

  <span class="label" style="left:42px;top:718px">Liability Deducible:</span>
  <span class="check" style="left:42px;top:753px"></span>
  <span class="label" style="left:81px;top:753px">$500</span>
  <span class="check" style="left:166px;top:753px"></span>
  <span class="label" style="left:205px;top:753px">$1,000</span>
  <span class="check" style="left:326px;top:753px"></span>
  <span class="label" style="left:367px;top:753px">$2,500</span>
  <span class="check" style="left:490px;top:753px"></span>
  <span class="label" style="left:530px;top:753px">$5,000</span>

  <span class="label" style="left:42px;top:788px">Physical Damage Deductible:</span>
  <span class="check" style="left:42px;top:823px"></span>
  <span class="label" style="left:68px;top:823px">$500</span>
  <span class="check" style="left:166px;top:823px"></span>
  <span class="label" style="left:205px;top:823px">$1,000</span>
  <span class="check" style="left:326px;top:823px"></span>
  <span class="label" style="left:367px;top:823px">$2,500</span>
  <span class="check" style="left:490px;top:823px"></span>
  <span class="label" style="left:530px;top:823px">$5,000</span>

  <span class="label" style="left:42px;top:873px">Driving radius:</span>
  <span class="field" style="left:149px;top:873px;width:420px"></span>
  <span class="label" style="left:42px;top:908px">How many years have you had your own continuous commercial auto insurance coverage for the current business name?</span>
  <span class="field tall" style="left:42px;top:928px;width:854px;height:30px"></span>

  <span class="label" style="left:42px;top:978px">Do any of your vehicles travel across state lines?</span>
  <span class="label" style="left:421px;top:978px">Yes</span>
  <span class="check" style="left:462px;top:978px"></span>
  <span class="label" style="left:530px;top:978px">No</span>
  <span class="check" style="left:571px;top:978px"></span>
  <span class="label" style="left:42px;top:1013px">If yes, please list all states in which vehicles operate:</span>
  <span class="field" style="left:405px;top:1013px;width:491px"></span>

  <span class="label" style="left:42px;top:1048px">What is the maximum radius traveled for your customer's business?</span>
  <span class="label" style="left:42px;top:1083px">0-25 miles</span>
  <span class="check" style="left:119px;top:1083px"></span>
  <span class="label" style="left:149px;top:1083px">26-50 miles</span>
  <span class="check" style="left:234px;top:1083px"></span>
  <span class="label" style="left:259px;top:1083px">51-75 miles</span>
  <span class="check" style="left:345px;top:1083px"></span>
  <span class="label" style="left:378px;top:1083px">76-100 miles</span>
  <span class="check" style="left:476px;top:1083px"></span>
  <span class="label" style="left:530px;top:1083px">101-150 miles</span>
  <span class="label" style="left:42px;top:1117px">151-200 miles</span>
  <span class="check" style="left:155px;top:1117px"></span>
  <span class="label" style="left:205px;top:1117px">201-300 miles</span>
  <span class="check" style="left:322px;top:1117px"></span>
  <span class="label" style="left:367px;top:1117px">300+ miles</span>
  <span class="check" style="left:460px;top:1117px"></span>

  <span class="label" style="left:42px;top:1152px">Would you like physical damage coverage for this vehicle? (should be for each vehicle listed)</span>
</main>
</body>
</html>
```